Not another boring Business Card Design Project

This is not another boring Business Card Design Project.

We are looking for the weirdest, wackiest most boundary pushing designs that you can come up with.

If you believe that design can be fun, energetic, crazy, unpredictable, beautiful and eye-catching then read on… this project is for you.

We are Wendel Prask and we print plastic cards.

We are running a Plastic Card Design Competition.

And we need a plastic card to advertise the competition to graphic designers just like you.

The design needs to make your average designers’ jaws drop and their eyes pop out.

You can do what you wish with the card design, so long as it stands out.

We like these designs, designs that stretch the boundaries and become something beyond just another business card:

http://quorvexpixels.net/wp-content/uploads/2009/03/b48.jpg
Designer - http://www.plumtorics.com/

http://quorvexpixels.net/wp-content/uploads/2009/03/b41.jpg
Designer - http://ferrandokaltz.com/

http://images.pixelhive.com/designs/44195_732292_37774_thumbnail.jpg
Designer- Lumbro Works at Pixel Hive

http://images.pixelhive.com/designs/44195_717529_37774_thumbnail.jpg
Designer - Lumbro Works at Pixel Hive

http://quorvexpixels.net/wp-content/uploads/2009/03/b11.jpg
Designer - http://www.qv7design.com/

http://quorvexpixels.net/wp-content/uploads/2009/03/b16.jpg
Designer - http://www.wobblethistle.com/

Reason: A number of designers have said they want to submit designs and haven't yet done so, we want to give them time.

Reason: We've extended the deadline by 4 days for those who want to submit their designs over the weekend and give ourselves time to judge them

Plastic

Requirements
Nice to have
• The design needs to contain this link: zq.example/Rk7pLx and any other detail that will encourage competition entry. The design will be printed on plastic.
Should not have
• No borders (when plastic cards are punched to shape and size there is movement of 1 - 2mm, borders highlight this movement).

Keep text 3mm away from edges of the cards.

Please don't create designs to be produced on clear/transparent plastic.

```html
<!DOCTYPE html>
<html lang="en">
<head>
<meta charset="utf-8">
<title>Wild Tumblers – Plastic Card Contest</title>
<link rel="stylesheet" href="https://fonts.googleapis.com/css2?family=Rye&family=Sniglet:wght@400;800&display=swap">
<style>
  :root {
    --paper: #ece3cb;
    --paper-warm: #e4cfa6;
    --paper-green: #d9d6b4;
    --rust: #7c3a22;
    --cocoa: #4a3027;
    --white: #ffffff;
  }
  html, body {
    margin: 0;
    width: 1200px;
    height: 753px;
    overflow: hidden;
    background: #ffffff;
  }
  .card {
    position: relative;
    width: 1185px;
    height: 744px;
    border-radius: 24px;
    overflow: hidden;
    background:
      radial-gradient(ellipse at 62% 30%, var(--paper-warm) 0%, rgba(228,207,166,0) 55%),
      radial-gradient(ellipse at 20% 20%, var(--paper-green) 0%, rgba(217,214,180,0) 60%),
      var(--paper);
  }
  .acrobat-photo {
    position: absolute;
    left: 548px;
    top: 0;
    width: 280px;
    height: 340px;
    border-radius: 40% 40% 45% 45%;
    background: radial-gradient(ellipse at 50% 50%, #6b4a3c 0%, #8d6a58 45%, rgba(141,106,88,0) 72%);
  }
  .contest-label {
    position: absolute;
    left: 88px;
    top: 172px;
    transform: translate(-50%, -50%) rotate(-90deg);
    font-family: "Sniglet", sans-serif;
    font-weight: 800;
    font-size: 17px;
    letter-spacing: 1px;
    color: var(--rust);
    white-space: nowrap;
  }
  .star-rule {
    position: absolute;
    left: 65px;
    top: 358px;
    width: 1055px;
    height: 17px;
    background: var(--rust);
  }
  .star-rule span {
    position: absolute;
    top: -3px;
    color: var(--white);
    font-size: 14px;
    line-height: 22px;
  }
  .link-band {
    position: absolute;
    left: 65px;
    top: 388px;
    width: 1055px;
    height: 87px;
    background: var(--cocoa);
    display: flex;
    align-items: center;
    justify-content: center;
  }
  .contest-link {
    font-family: "Sniglet", sans-serif;
    font-weight: 800;
    font-size: 64px;
    color: var(--white);
    letter-spacing: 1px;
  }
  .divider {
    position: absolute;
    top: 490px;
    width: 3px;
    height: 238px;
    background: var(--cocoa);
  }
  .badge {
    position: absolute;
    top: 492px;
    width: 240px;
    height: 240px;
    overflow: visible;
  }
  .badge text { fill: var(--rust); }
  .badge .arc-word { font-family: "Sniglet", sans-serif; font-size: 38px; letter-spacing: 2px; }
  .badge .big-word { font-family: "Rye", serif; font-size: 52px; }
  .badge .star { font-family: "Sniglet", sans-serif; font-size: 26px; }
  .event-name {
    position: absolute;
    left: 300px;
    top: 500px;
    width: 590px;
    height: 225px;
    margin: 0;
    display: flex;
    flex-direction: column;
    align-items: center;
    justify-content: space-between;
    font-family: "Sniglet", sans-serif;
    font-weight: 800;
    color: var(--rust);
    line-height: 1;
  }
  .event-name span { font-size: 92px; letter-spacing: 8px; }
</style>
</head>
<body>
<main class="card">
  <div class="acrobat-photo" role="img" aria-label="Photo of an aerial acrobat hanging upside down from a trapeze"></div>

  <div class="contest-label">★ ENTER THE CONTEST ★</div>

  <div class="star-rule">
    <span style="left:450px">★</span>
    <span style="left:517px;font-size:20px;top:-5px">★</span>
    <span style="left:594px">★</span>
  </div>

  <div class="link-band"><span class="contest-link">zq.example/Rk7pLx</span></div>

  <svg class="badge" style="left:42px" viewBox="0 0 240 240" aria-label="Have a NOW look!">
    <defs>
      <path id="arc-top-left" d="M 30 125 A 90 90 0 0 1 210 125"/>
      <path id="arc-bottom-left" d="M 22 125 A 98 98 0 0 0 218 125"/>
    </defs>
    <text class="arc-word"><textPath href="#arc-top-left" startOffset="50%" text-anchor="middle">have a</textPath></text>
    <text class="star" x="8" y="130">★</text>
    <text class="big-word" x="121" y="140" text-anchor="middle">NOW</text>
    <text class="star" x="210" y="130">★</text>
    <text class="arc-word"><textPath href="#arc-bottom-left" startOffset="50%" text-anchor="middle">look!</textPath></text>
  </svg>

  <div class="divider" style="left:278px"></div>

  <h1 class="event-name"><span>WILD</span><span>TUMBLERS</span></h1>

  <div class="divider" style="left:903px"></div>

  <svg class="badge" style="left:905px" viewBox="0 0 240 240" aria-label="Show and FREE popcorn">
    <defs>
      <path id="arc-top-right" d="M 30 125 A 90 90 0 0 1 210 125"/>
      <path id="arc-bottom-right" d="M 22 125 A 98 98 0 0 0 218 125"/>
    </defs>
    <text class="arc-word"><textPath href="#arc-top-right" startOffset="50%" text-anchor="middle">show &amp;</textPath></text>
    <text class="star" x="10" y="130">★</text>
    <text class="big-word" x="121" y="140" text-anchor="middle">FREE</text>
    <text class="star" x="212" y="130">★</text>
    <text class="arc-word"><textPath href="#arc-bottom-right" startOffset="50%" text-anchor="middle">popcorn</textPath></text>
  </svg>
</main>
</body>
</html>
```